Postcard Design

We are Professional, quick and efficient. We are State Licensed and Insured. Gas•Water•Sewer Specializing in all of the customers plumbing needs. We accept credit cards. The law in Louisiana is that I have company address, and license number on all advertising. License number is RKT 4291. Address is 52907 north elm ave. Cut Off, La. 70218

```html
<!DOCTYPE html>
<html lang="en">
<head>
<meta charset="utf-8">
<title>Dufrene Plumbing – Postcard</title>
<link rel="stylesheet" href="https://fonts.googleapis.com/css2?family=Archivo+Black&family=Cinzel:wght@500&family=Noto+Serif:ital,wght@0,700;1,700&family=Roboto:wght@700;900&display=swap">
<style>
  :root {
    --navy: #0b3a72;
    --blue-mid: #0f5fa8;
    --sky: #1ea6e4;
    --red: #c8242b;
    --red-deep: #b01c22;
    --white: #ffffff;
    --ink: #13306a;
    --yellow: #ffe21a;
    --skin: #f2c59a;
    --denim: #2f5e9e;
  }
  * { margin: 0; padding: 0; box-sizing: border-box; }
  html, body { width: 1200px; height: 563px; overflow: hidden; background: #e9ebee; }
  .postcard {
    position: relative;
    width: 1200px;
    height: 563px;
    overflow: hidden;
    background: var(--red);
  }
  .sky-panel {
    position: absolute; left: 0; top: 0; width: 1200px; height: 292px;
    background: radial-gradient(ellipse 60% 90% at 78% 30%, var(--sky) 0%, var(--blue-mid) 55%, var(--navy) 100%);
  }
  .service-band {
    position: absolute; left: 0; top: 285px; width: 1200px; height: 107px;
    background: var(--white);
    border-top: 4px solid var(--red);
  }
  .service-band::before {
    content: ""; position: absolute; left: 0; top: 0; width: 100%; height: 3px; background: var(--navy);
  }
  .call-panel {
    position: absolute; left: 0; top: 392px; width: 1200px; height: 171px;
    background: linear-gradient(180deg, var(--red) 0%, var(--red-deep) 100%);
  }
  .brand {
    position: absolute; left: 58px; top: 22px; color: var(--white);
  }
  .brand-name {
    font-family: "Archivo Black", sans-serif;
    font-size: 92px; line-height: 1; letter-spacing: 1px;
  }
  .brand-trade {
    font-family: "Archivo Black", sans-serif;
    font-size: 50px; line-height: 1; margin-top: 2px; margin-left: 28px; letter-spacing: 2px;
  }
  .brand-lines {
    font-family: "Cinzel", serif; font-weight: 500;
    font-size: 24px; line-height: 1.2; margin-top: 8px; margin-left: 30px; letter-spacing: 2px;
  }
  .services {
    position: absolute; left: 44px; top: 222px; display: flex; gap: 34px;
  }
  .service { width: 138px; text-align: center; }
  .service-tab {
    width: 108px; height: 108px; margin: 0 auto; border-radius: 50%;
    background: var(--white); border: 4px solid var(--red);
    display: flex; align-items: center; justify-content: center;
  }
  .service-photo { width: 84px; height: 84px; border-radius: 50%; }
  .photo-heater { background: radial-gradient(circle, #d8dde3 0%, #8fb9d8 100%); }
  .photo-sewer { background: radial-gradient(circle, #55585e 0%, #1d1f23 100%); }
  .photo-leak { background: radial-gradient(circle, #e2a070 0%, #a65a2e 100%); }
  .photo-tools { background: radial-gradient(circle, #f0f0f0 0%, #c44 100%); }
  .service-label {
    font-family: "Roboto", sans-serif; font-weight: 900;
    color: var(--ink); font-size: 15px; line-height: 1.05; margin-top: 4px; text-transform: uppercase;
  }
  .mascot {
    position: absolute; left: 820px; top: 28px; width: 250px; height: 455px;
    border-radius: 110px 110px 40px 40px;
    background: linear-gradient(180deg, var(--skin) 0%, var(--white) 30%, var(--denim) 55%, var(--denim) 85%, #a8794a 100%);
  }
  .callout { position: absolute; left: 58px; top: 402px; color: var(--white); }
  .callout-headline {
    font-family: "Noto Serif", serif; font-weight: 700; font-size: 36px; line-height: 1.05;
  }
  .callout-sub {
    font-family: "Noto Serif", serif; font-style: italic; font-weight: 700; font-size: 26px; line-height: 1.1;
  }
  .callout-phone {
    display: flex; align-items: center; gap: 8px;
    font-family: "Roboto", sans-serif; font-weight: 900; font-size: 44px; color: var(--yellow); line-height: 1.05;
  }
  .phone-icon { width: 34px; height: 34px; }
  .callout-address {
    font-family: "Roboto", sans-serif; font-weight: 700; font-size: 20px; line-height: 1.2; margin-top: 2px;
  }
  .license {
    position: absolute; left: 835px; top: 500px; color: var(--white);
    font-family: "Noto Serif", serif; font-size: 17px; font-weight: 700;
  }
</style>
</head>
<body>
<main class="postcard">
  <div class="sky-panel"></div>
  <div class="service-band"></div>
  <div class="call-panel"></div>

  <header class="brand">
    <h1 class="brand-name">Dufrene</h1>
    <div class="brand-trade">PLUMBING</div>
    <div class="brand-lines">GAS | WATER | SEWAGE</div>
  </header>

  <section class="services">
    <div class="service">
      <div class="service-tab"><div class="service-photo photo-heater" role="img" aria-label="Photo of a tankless water heater with splashing water"></div></div>
      <div class="service-label">Water<br>Heating</div>
    </div>
    <div class="service">
      <div class="service-tab"><div class="service-photo photo-sewer" role="img" aria-label="Photo of a round sewer manhole cover"></div></div>
      <div class="service-label">Sewer<br>Repair</div>
    </div>
    <div class="service">
      <div class="service-tab"><div class="service-photo photo-leak" role="img" aria-label="Photo of a leaking copper pipe joint"></div></div>
      <div class="service-label">Leakage<br>Repair</div>
    </div>
    <div class="service">
      <div class="service-tab"><div class="service-photo photo-tools" role="img" aria-label="Photo of plumbing tools: wrenches and pliers"></div></div>
      <div class="service-label">Remodelling</div>
    </div>
  </section>

  <div class="mascot" role="img" aria-label="Cartoon plumber in cap and blue overalls holding a large pipe wrench and a plunger"></div>

  <section class="callout">
    <h2 class="callout-headline">Need A Plumber?</h2>
    <div class="callout-sub">Call NOW!</div>
    <div class="callout-phone">
      <svg class="phone-icon" viewBox="0 0 36 36" aria-hidden="true">
        <circle cx="18" cy="18" r="16" fill="none" stroke="var(--yellow)" stroke-width="3"/>
        <path d="M12 10 q-3 2 -1 7 q3 7 9 9 q4 1 6 -2 l-3 -3 q-2 1 -3 0 q-3 -2 -5 -5 q-1 -1 0 -3 z" fill="var(--yellow)"/>
      </svg>
      <span>+1 985-555-0147</span>
    </div>
    <div class="callout-address">52907 north elm ave. Cut Off, La. 70218</div>
  </section>

  <div class="license">License number - RKT 4291</div>
</main>
</body>
</html>
```